Varnek Group Business Card

Varnek Group — Business Card Design Brief
Overview
Design a double-sided business card for Varnek Group that highlights our two service arms: Varnek Communications (telecommunications) and Varnek Energy (business energy solutions). The card should feel smart and stand out when handed to clients.

Objectives
Showcase our areas of specialty clearly.
Reflect the overall Varnek / Varnek Group brand while acknowledging both arms.
Explore using both logos (Communications + Energy) or one unified logo, depending on the design.

Deliverables
One double-sided business card design (front + back).

Content & Copy
Front (preferred): Logo: Varnek / Varnek Group
Descriptor: Business Communications | Business Energy
Back:My contact details and company details
Core products: Business Mobile • Telephony • Internet • Business Energy Solutions

Brand & Visual Direction
We have a group logo currently tailored more toward telecoms, plus a separate Varnek Energy logo.
Please explore layouts that use both logos or just one, whichever works best.
Color: I wouldn't mind seeing an option using our the Blue/Purple gradient from our website (varnek-example.co.uk), but also open to non-gradient approaches and other colours..

Overall look: Smart, modern, and distinctive.
Format & Print Specs
Double-sided business card format. (Use a standard size

Must-Haves
Front: Varnek wording or Varnek Group wording with atleast 1 logo also on front “Business Communications | Business Energy.”

Back: Contact + company details and core products.
A design that stands out while remaining professional.

Nice-to-Have Options
A gradient version using our site’s Blue/Purple gradient.
A non-gradient version.
A dual-logo treatment versus a single-logo treatment.

Thanks
Dominic

```html
<!DOCTYPE html>
<html lang="en">
<head>
<meta charset="utf-8">
<title>Varnek Group Business Card</title>
<link href="https://fonts.googleapis.com/css2?family=Lato:wght@400;700;900&display=swap" rel="stylesheet">
<style>
  :root {
    --backdrop: #2c2e30;
    --navy: #1c1566;
    --purple: #9a12c9;
    --blue: #1a5ed8;
    --sky: #1bb0e0;
    --line-blue: #2266cc;
    --white: #ffffff;
    --text-soft: #e8e6f5;
  }
  * { box-sizing: border-box; margin: 0; padding: 0; }
  html, body { width: 1200px; height: 1122px; overflow: hidden; }
  body {
    background: var(--backdrop);
    font-family: "Lato", sans-serif;
    position: relative;
  }
  .card {
    position: absolute;
    width: 620px;
    height: 390px;
    border-radius: 22px;
    overflow: hidden;
    box-shadow: 0 14px 30px rgba(0,0,0,0.45);
  }
  /* Front */
  .card-front {
    left: 110px; top: 100px;
    background: linear-gradient(90deg, var(--purple) 0%, #3a1490 32%, #1c1466 60%, #1b2a8a 85%, #1a4da4 100%);
  }
  .front-glow {
    position: absolute; left: -60px; top: 150px;
    width: 380px; height: 380px; border-radius: 50%;
    border: 38px solid rgba(170, 60, 230, 0.18);
  }
  .front-brand {
    position: absolute; left: 0; right: 0; top: 120px;
    display: flex; align-items: center; justify-content: center; gap: 18px;
  }
  .brand-dot {
    width: 64px; height: 64px; border-radius: 50%;
    background: linear-gradient(135deg, var(--blue), var(--sky));
  }
  .front-brand .brand-name {
    font-weight: 900; font-size: 74px; letter-spacing: 2px;
    color: var(--white);
  }
  .front-descriptor {
    position: absolute; left: 0; right: 0; top: 250px;
    text-align: center; color: var(--text-soft);
    font-size: 15px; letter-spacing: 2.5px; text-transform: uppercase;
  }
  .front-descriptor strong { font-weight: 900; color: var(--white); }

  /* Back */
  .card-back {
    left: 470px; top: 620px;
    background: var(--white);
    color: var(--navy);
  }
  .back-brand {
    position: absolute; right: 32px; top: 32px;
    display: flex; align-items: center; gap: 12px;
  }
  .back-brand .brand-dot { width: 42px; height: 42px; }
  .back-brand .brand-name { font-weight: 900; font-size: 44px; letter-spacing: 1px; color: var(--navy); }
  .rule { position: absolute; height: 1.5px; background: var(--line-blue); }
  .rule-top { left: 32px; right: 32px; top: 112px; }
  .rule-mid { left: 32px; width: 210px; top: 226px; }
  .rule-bottom { left: 32px; right: 32px; top: 330px; }
  .company-details {
    position: absolute; right: 32px; top: 124px;
    text-align: right; font-size: 14.5px; line-height: 1.35; color: var(--navy);
    font-style: normal;
  }
  .person { position: absolute; left: 32px; top: 150px; }
  .person-name { font-weight: 900; font-size: 34px; letter-spacing: 0.5px; line-height: 1.15; }
  .person-role { font-size: 17px; color: var(--purple); margin-top: 2px; }
  .contacts {
    position: absolute; left: 32px; top: 240px;
    list-style: none; font-size: 15px; line-height: 1.65;
  }
  .contacts li { display: flex; align-items: center; gap: 10px; }
  .contacts svg { width: 14px; height: 14px; flex: none; }
  .icon-fill { fill: var(--purple); }
  .icon-line { fill: none; stroke: var(--purple); stroke-width: 2; }
  .core-products {
    position: absolute; left: 32px; right: 32px; top: 344px;
    font-size: 11.5px; letter-spacing: 0; text-transform: uppercase; white-space: nowrap;
  }
  .core-products strong { font-weight: 900; }
  .core-products .sep { color: var(--purple); margin: 0 3px; }
</style>
</head>
<body>
  <section class="card card-front" aria-label="Card front">
    <div class="front-glow"></div>
    <div class="front-brand">
      <span class="brand-dot"></span>
      <span class="brand-name">VARNEK</span>
    </div>
    <p class="front-descriptor">Business <strong>Communications</strong> + Business <strong>Energy</strong></p>
  </section>

  <section class="card card-back" aria-label="Card back">
    <div class="back-brand">
      <span class="brand-dot"></span>
      <span class="brand-name">VARNEK</span>
    </div>
    <div class="rule rule-top"></div>
    <address class="company-details">
      Varnek Communications + Energy<br>
      24 Halden Row, Manchester<br>
      England, M0 0XX
    </address>
    <div class="person">
      <h1 class="person-name">DANIEL ORRIN</h1>
      <p class="person-role">Managing Director &amp; CEO</p>
    </div>
    <div class="rule rule-mid"></div>
    <ul class="contacts">
      <li><svg viewBox="0 0 24 24"><path class="icon-fill" d="M6.6 10.8a15 15 0 0 0 6.6 6.6l2.2-2.2a1 1 0 0 1 1-.25 11.4 11.4 0 0 0 3.6.57 1 1 0 0 1 1 1V20a1 1 0 0 1-1 1A17 17 0 0 1 3 4a1 1 0 0 1 1-1h3.5a1 1 0 0 1 1 1c0 1.25.2 2.45.57 3.57a1 1 0 0 1-.25 1z"/></svg>+44 0161 555 0148</li>
      <li><svg viewBox="0 0 24 24"><rect class="icon-fill" x="2" y="5" width="20" height="14" rx="1.5"/><path d="M3 6l9 7 9-7" fill="none" stroke="#fff" stroke-width="2"/></svg>info@varnek-example.co.uk</li>
      <li><svg viewBox="0 0 24 24"><circle class="icon-line" cx="12" cy="12" r="9.5"/><path class="icon-line" d="M2.5 12h19M12 2.5c3 3 3 16 0 19M12 2.5c-3 3-3 16 0 19"/></svg>varnek-example.co.uk</li>
    </ul>
    <div class="rule rule-bottom"></div>
    <p class="core-products"><strong>Core products:</strong> Business Mobile<span class="sep">•</span>Telephony<span class="sep">•</span>Internet<span class="sep">•</span>Business Energy Solutions</p>
  </section>
</body>
</html>
```